Design for Huddle app (online tool) (#102244)

Url of the app: http://huddle.moorfinch.dk

It currently has 3 main parts:
- Front: http://tealmarsh.dk/screencast/2015-12-01_12-53-36.png
- Dashboard: http://tealmarsh.dk/screencast/2015-12-01_12-54-16.png
- Meeting page: http://tealmarsh.dk/screencast/2015-12-01_12-54-53.png

The idea of the app is to have virtual meetings with other people, to take notes/minutes online and to share what is written.

Unregistered users can see only the front.

Registered users can see front, their own dashboard and the meetings which they created or to which they were invited.

The meeting itself has two roles - minute taker an attendee. The attendee can edit only the agenda so he should have different view for the other parts of the meeting compared to the minute taker who can edit everything.

In this doc it is described what are the elements per page which we want to have
https://files.quillnest.example/doc/7vKp2RtXw9LmQa4Hs8NcYe3BdZu6JfTgPo1iWxEk/edit?usp=sharing

As you can see, there is some inconsistency between the front page and the rest of the app. We would like to make it look professional and consistent on all places.

Goal: Get new responsive design where all main parts(front page, dashboard page, meeting page and profile page) will be consistent with each other.

The design should be clean, simple and with very friendly UX.
Updates

Industry/Entity Type

Online

Number of Pages Required

3 page

Font styles to use
Sans Serif

Requirements
Must have
• - Clean and simple
• - Very friendly UX

```html
<!DOCTYPE html>
<html lang="en">
<head>
<meta charset="utf-8">
<title>Moorfinch Huddle – Dashboard</title>
<link rel="stylesheet" href="https://fonts.googleapis.com/css2?family=Open+Sans:wght@300;400&display=swap">
<style>
  :root {
    --page-bg: #ffffff;
    --text-muted: #a8a8a8;
    --text-accent: #5ea6f6;
    --band-blue: #6aaefc;
    --band-text: #ffffff;
    --card-grey: #ebebeb;
    --button-border: #5a8fd0;
  }
  * { box-sizing: border-box; margin: 0; padding: 0; }
  html, body { width: 1200px; height: 719px; overflow: hidden; background: var(--page-bg); }
  body { font-family: "Open Sans", sans-serif; font-weight: 300; color: var(--text-muted); position: relative; }

  .app-header { position: absolute; top: 54px; left: 0; width: 1200px; height: 36px; }
  .app-title { position: absolute; left: 435px; top: 4px; font-size: 22px; line-height: 28px; font-weight: 300; color: var(--text-muted); }
  .new-meeting-button {
    position: absolute; left: 624px; top: 0; width: 136px; height: 37px;
    border: 1px solid var(--button-border); border-radius: 2px; background: var(--page-bg);
    font: 300 16.5px/35px "Open Sans", sans-serif; color: var(--text-muted); text-align: center;
  }

  .section-title { position: absolute; left: 75px; top: 124px; font-size: 22px; line-height: 28px; font-weight: 300; letter-spacing: 0.3px; color: #b9b9b9; }

  .dashboard-nav { position: absolute; left: 68px; top: 155px; width: 1064px; height: 31px; display: flex; gap: 1px; background: var(--page-bg); }
  .nav-item { background: var(--band-blue); color: var(--band-text); font-size: 15.5px; line-height: 31px; font-weight: 400; white-space: nowrap; }
  .nav-search { width: 537px; padding-left: 7px; }
  .nav-filed { width: 140px; text-align: center; }
  .nav-own { width: 164px; text-align: center; }
  .nav-attended { width: 220px; text-align: center; }

  .meeting-list { position: absolute; left: 68px; top: 226px; width: 1064px; list-style: none; }
  .meeting-card { position: absolute; left: 0; width: 1064px; padding-left: 13px; }
  .meeting-card.is-shaded { background: var(--card-grey); color: var(--text-muted); }
  .meeting-card.is-accent { color: var(--text-accent); }
  .meeting-line { font-size: 15.5px; line-height: 22px; white-space: nowrap; }
  .meeting-line.is-small { font-size: 14.5px; }
  .attendee-lead { color: var(--text-accent); }

  .card-one { top: 0; height: 101px; padding-top: 13px; }
  .card-one .meeting-line { line-height: 24.5px; }
  .card-two { top: 124px; height: 90px; }
  .card-three { top: 214px; height: 117px; padding-top: 14px; }
  .card-four { top: 354px; height: 70px; }

  .more-button {
    position: absolute; left: 67px; top: 665px; width: 90px; height: 31px;
    background: var(--band-blue); color: var(--band-text); border: 0;
    font: 400 15.5px/31px "Open Sans", sans-serif; text-align: center;
  }
</style>
</head>
<body>
  <header class="app-header">
    <h1 class="app-title">Moorfinch Huddle</h1>
    <div class="new-meeting-button">New Meeting</div>
  </header>

  <h2 class="section-title">DASHBOARD</h2>

  <nav class="dashboard-nav">
    <div class="nav-item nav-search">Search by attendees'names'meeting title,date,location.Fx '12.11.2015'</div>
    <div class="nav-item nav-filed">Filed meetings</div>
    <div class="nav-item nav-own">My own meetings</div>
    <div class="nav-item nav-attended">Meeting which i attended</div>
  </nav>

  <ul class="meeting-list">
    <li class="meeting-card is-shaded card-one">
      <p class="meeting-line">Tom Title Test</p>
      <p class="meeting-line"><span class="attendee-lead">Tomas Varga &lt;tomas@moorfinch.dk&gt;</span><span class="is-small">,LenaMarkov&lt;lena@moorfinch.dk&gt;,&lt;oren@moorfinch.dk&gt;</span></p>
      <p class="meeting-line">25.11.2015 14:19 @Lovech</p>
    </li>
    <li class="meeting-card is-accent card-two">
      <p class="meeting-line">fdsfdsfs</p>
      <p class="meeting-line">26.11.2015-15:57 @oro</p>
      <p class="meeting-line">Tomas Vagra&lt;tvarga@moorfinch.dk&gt;</p>
    </li>
    <li class="meeting-card is-shaded card-three">
      <p class="meeting-line">PM Weekly meeting</p>
      <p class="meeting-line">25.11.2015 14:19-14:19 @Meeting place</p>
      <p class="meeting-line is-small">&lt;nils@moorfinch.dk&gt;,Oren Dalby&lt;oren@moorfinch.dk&gt;,&lt;tomas@moorfinch.dk&gt;Karl Brenn.Mads Ellery,</p>
      <p class="meeting-line is-small">&lt;nils@moorfinch.dk&gt;,&lt;lena@moorfinch.dk&gt;</p>
    </li>
    <li class="meeting-card is-accent card-four">
      <p class="meeting-line">Testing Names</p>
      <p class="meeting-line">25.11.2015 14:19-14:19 @Meeting place</p>
      <p class="meeting-line">TomasVagra,Tomas&lt;tomsa@moorfinch.dk&gt;Lena Markov,&lt;orchid7@mailbox.example&gt;</p>
    </li>
  </ul>

  <div class="more-button">dadad</div>
</body>
</html>
```